Webdesign for blog, vlog and website
The designs for my website were better than what I expected when I started this contest. I knew I needed a call-to-action on my homepage, but I thought it wouldn't be possible and I didn't ask for it either. But Ignacio did it anyway. Furthermore, his design looked very good. For that reason I selected him as winner already before I should. I am very happy.

```html
<!DOCTYPE html>
<html lang="en">
<head>
<meta charset="utf-8">
<title>Ideora – Blog &amp; Vlog</title>
<link href="https://fonts.googleapis.com/css2?family=Bebas+Neue&family=Roboto:wght@300;400;500&display=swap" rel="stylesheet">
<style>
:root{
  --topbar:#1f3b5f;
  --nav:#1f2229;
  --accent:#f6a623;
  --accent-light:#f8d24e;
  --ink:#222;
  --body:#444;
  --muted:#888;
  --white:#fff;
}
*{margin:0;padding:0;box-sizing:border-box}
html,body{width:888px;height:1200px;overflow:hidden;background:var(--white)}
body{position:relative;font-family:'Roboto',sans-serif;color:var(--ink)}
.abs{position:absolute}
.topbar{left:0;top:0;width:888px;height:26px;background:var(--topbar);overflow:hidden}
.topbar svg{position:absolute;left:0;top:0}
.btn-top{top:6px;height:16px;background:var(--accent);color:var(--white);font-size:8px;display:flex;align-items:center;justify-content:center;border-radius:1px}
.login{left:720px;width:42px}
.register{left:766px;width:49px}
.lang-caret{left:836px;top:11px}
.flag{left:848px;top:4px;width:25px;height:18px}
.nav{left:0;top:26px;width:888px;height:41px;background:var(--nav)}
.brand{left:13px;top:37px;display:flex;align-items:center;gap:4px;color:var(--white);font-size:15px;font-weight:500}
.brand-dot{width:14px;height:14px;border-radius:50%;background:var(--white)}
.nav-item{top:39px;display:flex;align-items:center;gap:6px;color:var(--white);font-size:9px;font-weight:500}
.tab{left:275px;top:84px;height:22px;width:94px}
.tab span{position:absolute;left:15px;top:6px;color:var(--white);font-size:8px;font-weight:500}
.hero{left:275px;top:111px;width:296px;height:151px;background:linear-gradient(120deg,#d9dfe2,#c4ccd1 55%,#a9b7c2)}
.hero-title{left:275px;top:200px;width:204px;height:40px}
.hero-title svg{position:absolute;left:0;top:0}
.hero-title p{position:absolute;left:6px;top:2px;font-family:'Bebas Neue',sans-serif;font-size:20px;line-height:18px;color:var(--nav)}
.action{top:271px;height:20px;background:var(--nav);color:var(--white);font-size:9px;font-weight:500;display:flex;align-items:center;gap:6px;padding-left:7px;border-radius:1px}
.share{top:274px;width:16px;height:16px;background:var(--nav);border-radius:1px}
.lead{left:278px;top:304px;width:295px;font-size:8px;line-height:9.6px;color:var(--ink)}
.feature{top:381px;height:173px;overflow:hidden}
.feature .band{position:absolute;left:0;bottom:0;width:100%;height:44px;background:rgba(20,20,20,.75)}
.feature .cat{position:absolute;left:10px;top:133px;font-family:'Bebas Neue',sans-serif;font-size:13px;color:var(--accent)}
.feature h2{position:absolute;left:10px;top:147px;font-family:'Bebas Neue',sans-serif;font-weight:400;font-size:20px;color:var(--white);white-space:nowrap}
.post-img{left:128px;width:171px;height:107px}
.post{left:313px;width:320px}
.post .cat{font-family:'Bebas Neue',sans-serif;font-size:11px;color:var(--accent);line-height:12px}
.post h3{font-family:'Bebas Neue',sans-serif;font-weight:400;font-size:16.5px;color:#333;line-height:16px;margin-top:3px;white-space:nowrap}
.post p{font-size:8px;line-height:9.6px;color:var(--body);margin-top:4px;padding-left:1px}
.post time{display:block;font-size:7px;font-weight:300;color:#666;margin-top:3px;padding-left:2px}
.footer{left:0;top:1066px;width:888px;height:134px;background:var(--nav);color:var(--white)}
.company{left:31px;top:1104px;font-size:8px;line-height:12.4px;font-weight:300}
.company strong{display:block;font-size:11px;font-weight:400;line-height:14px}
.newsletter{left:342px;top:1104px;font-size:8px;font-weight:300}
.email{left:340px;top:1118px;width:144px;height:26px;background:#0b0b0d;color:var(--white);font-size:11px;font-weight:500;padding:6px 7px}
.subscribe{left:489px;top:1122px;width:47px;height:19px;background:var(--accent);color:var(--nav);font-size:7px;font-weight:500;display:flex;align-items:center;justify-content:center;border-radius:1px}
.legal{left:0;top:1183px;width:888px;text-align:center;font-size:7px;font-weight:300}
</style>
</head>
<body>

<div class="abs topbar">
  <svg width="888" height="26" viewBox="0 0 888 26">
    <polygon points="237,0 345,0 370,26 262,26" fill="#f6a623"/>
    <polygon points="330,0 420,0 445,26 355,26" fill="#f8c53a"/>
    <polygon points="415,0 500,0 525,26 440,26" fill="#f3c82c"/>
    <polygon points="495,0 555,0 591,26 520,26" fill="#fde07a"/>
  </svg>
</div>
<div class="abs btn-top login">LOGIN</div>
<div class="abs btn-top register">REGISTER</div>
<svg class="abs lang-caret" width="8" height="5" viewBox="0 0 8 5"><polygon points="0,0 8,0 4,4" fill="#16263c"/></svg>
<svg class="abs flag" viewBox="0 0 25 18" role="img" aria-label="Language flag">
  <rect width="25" height="6" fill="#f7931e"/><rect y="6" width="25" height="6" fill="#fff"/><rect y="12" width="25" height="6" fill="#1e6ff0"/>
</svg>

<div class="abs nav"></div>
<div class="abs brand"><span class="brand-dot"></span>Ideora</div>

<div class="abs nav-item" style="left:296px">
  <svg width="16" height="13" viewBox="0 0 16 13"><polygon points="8,0 16,7 13.5,7 13.5,13 9.5,13 9.5,9 6.5,9 6.5,13 2.5,13 2.5,7 0,7" fill="#f6a623"/></svg>BLOG
</div>
<div class="abs nav-item" style="left:378px">
  <svg width="17" height="13" viewBox="0 0 17 13"><ellipse cx="7" cy="5" rx="7" ry="5" fill="#f6a623"/><ellipse cx="11" cy="8" rx="6" ry="4.5" fill="#f6a623"/><polygon points="3,8 2,12 7,9" fill="#f6a623"/></svg>FORUM
</div>
<div class="abs nav-item" style="left:458px">
  <svg width="13" height="13" viewBox="0 0 13 13"><path d="M3.5 5 Q6.5 0 9.5 5" stroke="#f6a623" stroke-width="1.5" fill="none"/><polygon points="0,5 13,5 11,13 2,13" fill="#f6a623"/></svg>SHOP
</div>
<div class="abs nav-item" style="left:523px">
  <svg width="13" height="13" viewBox="0 0 13 13"><circle cx="6.5" cy="6.5" r="6.5" fill="#f6a623"/><text x="6.5" y="10" text-anchor="middle" font-family="Roboto,sans-serif" font-weight="700" font-size="9" fill="#1f2229">?</text></svg>ABOUT
</div>

<div class="abs tab">
  <svg width="94" height="22" viewBox="0 0 94 22"><polygon points="0,0 73,0 94,22 0,22" fill="#1f2229"/></svg>
  <span>NEWEST VLOG</span>
</div>

<div class="abs hero" role="img" aria-label="Vlog still: presenter in a blue sports top talking in front of a light wall"></div>
<div class="abs hero-title">
  <svg width="204" height="40" viewBox="0 0 204 40"><polygon points="0,0 175,0 204,40 0,40" fill="#f6a623"/></svg>
  <p>LETS MOTIVATE EACH<br>OTHER TO KEEP EXERCISING</p>
</div>

<div class="abs action" style="left:278px;width:79px">
  <svg width="13" height="11" viewBox="0 0 13 11"><polygon points="0,0 13,0 13,8 5,8 2,11 2,8 0,8" fill="#f6a623"/></svg>COMMENT
</div>
<div class="abs action" style="left:362px;width:64px">
  <svg width="16" height="11" viewBox="0 0 16 11"><polygon points="4,1 13,5.5 4,10" fill="#f6a623"/></svg>VLOGS
</div>
<div class="abs share" style="left:477px"></div>
<div class="abs share" style="left:496px"></div>
<div class="abs share" style="left:515px"></div>
<div class="abs share" style="left:535px"></div>
<svg class="abs share" style="left:554px" viewBox="0 0 16 16"><rect width="16" height="16" fill="#1f2229"/><path d="M8 3.5v9M3.5 8h9" stroke="#fff" stroke-width="2.2"/></svg>

<p class="abs lead">Regularly we hear that we don’t exercise enough. But we also hear contradicting messages about what kind of movement would be the best. That is confusing and it doesn’t stimulate us to start exercising more. In this vlog I’ll give you some sugges­tions about how to handle contradicting messages about sports and health and just start to exercise more. And on top of that: like it too!</p>

<div class="abs feature" style="left:131px;width:307px;background:radial-gradient(ellipse at 52% 40%,#6e5546,#2a1d17 45%,#0d0a09 75%)" role="img" aria-label="Portrait of a public figure in a dark suit">
  <div class="band"></div>
  <span class="cat">PEOPLE</span>
  <h2>WHAT IS HARLOW’S IQ?</h2>
</div>
<div class="abs feature" style="left:447px;width:306px;background:linear-gradient(135deg,#7a3a1c,#b4552a 35%,#d89a3a 55%,#6d7a2c 75%,#8a6a45)" role="img" aria-label="Assorted foods: bread, meat, fish, vegetables and fruit">
  <div class="band"></div>
  <span class="cat">MEDIA</span>
  <h2>THIS IS OUTRAGEOUS. FRIGHTFUL QUACKERY</h2>
</div>

<div class="abs post-img" style="top:573px;background:linear-gradient(100deg,#5a3210,#b46a2a 25%,#2c3f7a 55%,#1c2a4e 80%,#0e0e14)" role="img" aria-label="Wall of television screens showing many images"></div>
<article class="abs post" style="top:573px">
  <div class="cat">MEDIA</div>
  <h3>THE MEDIA SHOULD BE SILENT AFTER THE NEXT TERRORIST ATTACK</h3>
  <p>I read a column in which Marten Vos argues that when there is another terrorist attack, news channels should go off the air instead of keep on repeating the same news. I was surprised about this column but after considering his idea I propose a less extreme idea that I think would be really helpful.</p>
  <time>Oct. 26, 2017</time>
</article>

<div class="abs post-img" style="top:690px;background:linear-gradient(90deg,#e6e6e4,#dcdcda 45%,#d9c9b5 50%,#e4e4e2 60%,#eaeae8)" role="img" aria-label="Vlog still: presenter with long hair against a white wall"></div>
<article class="abs post" style="top:693px;left:314px">
  <div class="cat">VLOG</div>
  <h3>CIVIL DISOBEDIENCE IS NOT JUST FOR FUN</h3>
  <p>Civil disobedience is a term that can be very convenient. If we don’t like the law at a certain moment, then we like to be civil disobedient so that the law doesn’t bother us. But in some cases civil disobedience can be very important and precisely for that reason we shouldn’t use this term too easily so that it doesn’t lose its power at moments in which we really need it.</p>
  <time>Oct. 26, 2017</time>
</article>

<div class="abs post-img" style="top:806px;background:linear-gradient(90deg,#dcdcdc,#e8e8e8 30%,#c72a2a 40%,#b81f1f 90%,#d8d8d8)" role="img" aria-label="Video platform sign on a light background"></div>
<article class="abs post" style="top:810px">
  <div class="cat">MEDIA</div>
  <h3>‘A 16-YEAR OLD BOY WAS KILLED WHILE DOING THE ‘CHOKING GAME’</h3>
  <p>Time and again we hear about problematic videos on VidStream: youngsters who beat others up, youngsters who are disrespectful towards the police, youngsters who jump on a train, etc. And last week we heard about another terrible accident that was the result of a challenge that was spread via VidStream:</p>
  <time>Oct. 26, 2017</time>
</article>

<footer class="abs footer"></footer>
<div class="abs company">
  <strong>Ideora</strong>
  Chamber of commerce: 50317724<br>
  VAT number: NL100283746B01<br>
  Email: info@ideora.nl<br>
  Phone: +31 (0)6-10284756
</div>
<div class="abs newsletter">Yes, I would like to receive the monthly Ideora newsletter</div>
<div class="abs email">E-Mail</div>
<div class="abs subscribe">SUBSCRIBE</div>
<div class="abs legal" style="color:#fff">User agreement | Privacy Policy | Terms of Service</div>

</body>
</html>
```